SilverLedgerOak - Double Sided Business Card

We are looking for design options or our business cards. We are a Business Solutions and HR solutions Provider - the theme is business, for this card.

Our brand colours are represented within our logo.

Details needed to be put on the front of the business card are:

Employees name: [Sample Name]
Role: [Sample Role]

Address: Suite 4 - Level 3/48 Halloran Avenue Parramatta NSW 2150
M: 0000 000 000
P: 1300 847 213
F: 1300 847 286
E: sample@silverledgeroak.com.au
www.silverledgeroak.com.au
Updates

Reason: Hello, could we please increase our deadline by 5 days. Thanking you, Tess

Target Market(s)

Business Owners, also Candidates looking for Employment

Industry/Entity Type

Business

Contact Information for Business Card

Role: [Sample Role]

M: 0000 000 000
P: 1300 847 213
F: 1300 847 286

Font styles to use
Sans Serif

Colors
3276b5
3176b5
0455a3
85abd2
cfdeed
ffffff
000000
1b1b1b
757575

Requirements
Must have
• Details needed to be put on the front of the business card are:
• Employees name: [Sample Name]
• Role: [Sample Role]
• Address: Suite 4 - Level 3/48 Halloran Avenue Parramatta NSW 2150
• M: 0000 000 000
• P: 1300 847 213
• F: 1300 847 286
• E: sample@silverledgeroak.com.au
• www.silverledgeroak.com.au
Nice to have
• Simplicity, clean and professional.

```html
<!DOCTYPE html>
<html lang="en">
<head>
<meta charset="utf-8">
<title>SilverLedgerOak – Business Card Front</title>
<link rel="stylesheet" href="https://fonts.googleapis.com/css2?family=Arimo:wght@400;700&display=swap">
<style>
  :root {
    --page: #ffffff;
    --card: #ffffff;
    --card-edge: #1b1b1b;
    --brand-navy: #233b8c;
    --text-grey: #4a4a4a;
    --title-grey: #555555;
    --mark-tint: #eef1f7;
  }
  html, body {
    margin: 0;
    padding: 0;
    width: 1200px;
    height: 709px;
    overflow: hidden;
    background: var(--page);
  }
  .card {
    position: absolute;
    left: 25px;
    top: 30px;
    width: 1148px;
    height: 638px;
    box-sizing: border-box;
    border: 1.5px solid var(--card-edge);
    background: var(--card);
    overflow: hidden;
    font-family: "Arimo", Arial, sans-serif;
  }
  .brand-mark-area {
    position: absolute;
    left: 727px;
    top: 466px;
    width: 400px;
    height: 104px;
    background: var(--mark-tint);
  }
  .identity {
    position: absolute;
    right: 95px;
    top: 62px;
    text-align: right;
  }
  .identity__name {
    margin: 0;
    font-size: 37px;
    font-weight: 700;
    line-height: 1.1;
    color: var(--brand-navy);
  }
  .identity__role {
    margin: 4px 0 0;
    font-size: 28px;
    font-weight: 400;
    line-height: 1.1;
    color: var(--title-grey);
  }
  .contact {
    position: absolute;
    left: 98px;
    top: 253px;
    margin: 0;
    padding: 0;
    list-style: none;
    font-size: 25px;
    line-height: 34.5px;
    color: var(--text-grey);
  }
  .website {
    position: absolute;
    left: 98px;
    top: 547px;
    margin: 0;
    font-size: 25px;
    color: var(--brand-navy);
  }
</style>
</head>
<body>
  <main class="card">
    <div class="brand-mark-area" role="img" aria-label="Faint brand mark decoration"></div>

    <header class="identity">
      <h1 class="identity__name">Daniel Foster</h1>
      <p class="identity__role">Managing Director</p>
    </header>

    <ul class="contact">
      <li>Address: Suite 4 - Level 3/48 Halloran Avenue Parramatta NSW 2150</li>
      <li>M: 0000 000 000</li>
      <li>P: 1300 847 213</li>
      <li>F: 1300 847 286</li>
      <li>E: sample@silverledgeroak.com.au</li>
    </ul>

    <p class="website">www.silverledgeroak.com.au</p>
  </main>
</body>
</html>
```